Coral Bay Dental Surgery Business Cards

Hi there

Can i please have a simple business card designed (front and back with a black background) using out white reverse logo and the same font used for the logo?
On the back we can just have the logo. Full details at the front part.
Here are the details:

Name of the surgery: Coral Bay | Dental Surgery
Name on the business card: Dr Owen Thackery
Credentials:
BDSc (KTL)
MSc Oral Implantology (Halvorsen, Frankfurt)
Fellow & Diplomate (Meridian Council of Restorative Prosthetics)

Email: owen.thackery@coralbaysmile.example
Address: 17 Lisgrove Rd Karrinyup
Website: coralbaysmile.example
Phone: 1800 316 482

We have attached our high res logo and a rudimentary version of the business card which is not necessarily what we want but gives all the details
We would like to have the print ready version. Thanks.

Contact Information for Business Card

website. credentials. qr code. address. phone number

Requirements
Must have
• QR code

```html
<!DOCTYPE html>
<html lang="en">
<head>
<meta charset="utf-8">
<title>Coral Bay Dental Surgery – Business Cards</title>
<link href="https://fonts.googleapis.com/css2?family=Montserrat:wght@400;500;700&display=swap" rel="stylesheet">
<style>
  :root {
    --bg: #3a3a3c;
    --card: #1a1a1b;
    --ink: #ffffff;
    --ink-soft: #e6e6e6;
    --rule: #bdbdbd;
    --pattern-a: #2b2b2d;
    --pattern-b: #0f0f10;
  }
  * { margin: 0; padding: 0; box-sizing: border-box; }
  html, body {
    width: 1200px; height: 758px; overflow: hidden;
    background: var(--bg);
    font-family: "Montserrat", sans-serif;
    color: var(--ink);
  }
  .sheet {
    position: relative; width: 1200px; height: 758px;
    display: flex; align-items: center; justify-content: center; gap: 40px;
  }
  .card {
    position: relative;
    width: 540px; height: 330px;
    border-radius: 22px;
    background: var(--card);
    box-shadow: 0 18px 40px rgba(0,0,0,.45);
    overflow: hidden;
  }

  /* Back of card */
  .card--back .pattern {
    position: absolute; inset: 0;
    background: linear-gradient(120deg, var(--pattern-a) 0%, #1c1c1e 45%, var(--pattern-b) 100%);
  }
  .card--back .wordmark {
    position: absolute; right: 60px; top: 50%; transform: translateY(-50%);
  }

  /* Wordmark */
  .wordmark { display: flex; align-items: center; gap: 14px; }
  .wordmark__dot {
    width: 46px; height: 46px; border-radius: 50%;
    border: 3px solid var(--ink);
    flex: none;
  }
  .wordmark__name {
    font-weight: 700; color: var(--ink);
    font-size: 19px; line-height: 1.25; letter-spacing: .06em;
    text-transform: uppercase;
  }

  /* Front of card */
  .card--front { display: flex; }
  .card--front .brand {
    width: 215px; display: flex; flex-direction: column;
    align-items: center; justify-content: center; gap: 18px;
  }
  .card--front .brand .wordmark { flex-direction: column; text-align: center; gap: 12px; }
  .card--front .brand .wordmark__dot { width: 80px; height: 80px; border-width: 5px; }
  .card--front .brand .wordmark__name { font-size: 16px; }
  .qr-code {
    width: 60px; height: 60px;
    background: var(--ink);
    border-radius: 4px;
    border: 5px solid var(--ink);
    box-shadow: inset 0 0 0 3px var(--card);
  }
  .divider { width: 1px; background: var(--rule); margin: 44px 0; }
  .details {
    flex: 1; padding: 46px 26px 40px 28px;
    display: flex; flex-direction: column;
  }
  .details__name {
    font-weight: 700; font-size: 24px; letter-spacing: .02em;
    text-transform: uppercase; margin-bottom: 10px;
  }
  .credentials { list-style: none; font-size: 12.5px; line-height: 1.55; color: var(--ink-soft); }
  .contacts { list-style: none; margin-top: 22px; font-size: 13px; line-height: 1; }
  .contacts li { display: flex; align-items: center; gap: 10px; margin-bottom: 9px; }
  .contacts svg { width: 16px; height: 16px; flex: none; }
</style>
</head>
<body>
<main class="sheet">

  <section class="card card--back" aria-label="Card back">
    <div class="pattern" role="img" aria-label="Embossed repeating brand pattern in gloss black"></div>
    <div class="wordmark">
      <span class="wordmark__dot"></span>
      <span class="wordmark__name">Coral Bay<br>Dental Surgery</span>
    </div>
  </section>

  <section class="card card--front" aria-label="Card front">
    <div class="brand">
      <div class="wordmark">
        <span class="wordmark__dot"></span>
        <span class="wordmark__name">Coral Bay<br>Dental Surgery</span>
      </div>
      <div class="qr-code" role="img" aria-label="QR code linking to www.coralbaysmile.example"></div>
    </div>
    <div class="divider"></div>
    <div class="details">
      <h1 class="details__name">Dr Owen Thackery</h1>
      <ul class="credentials">
        <li>BDSc (KTL)</li>
        <li>MSc Oral Implantology (Halvorsen, Frankfurt)</li>
        <li>Fellow &amp; Diplomate</li>
        <li>(Meridian Council of Restorative Prosthetics)</li>
      </ul>
      <ul class="contacts">
        <li>
          <svg viewBox="0 0 16 16" aria-hidden="true"><circle cx="8" cy="8" r="8" fill="#fff"/><path d="M8 3.5a3 3 0 0 0-3 3c0 2.2 3 6 3 6s3-3.8 3-6a3 3 0 0 0-3-3zm0 4.2a1.2 1.2 0 1 1 0-2.4 1.2 1.2 0 0 1 0 2.4z" fill="#1a1a1b"/></svg>
          17 Lisgrove Rd Karrinyup
        </li>
        <li>
          <svg viewBox="0 0 16 16" aria-hidden="true"><circle cx="8" cy="8" r="8" fill="#fff"/><path d="M5.2 4h1.6l.8 2-1 .8a5 5 0 0 0 2.6 2.6l.8-1 2 .8v1.6c0 .5-.4.9-.9.9A7 7 0 0 1 4.3 4.9c0-.5.4-.9.9-.9z" fill="#1a1a1b"/></svg>
          1800 316 482
        </li>
        <li>
          <svg viewBox="0 0 16 16" aria-hidden="true"><circle cx="8" cy="8" r="8" fill="#fff"/><rect x="4" y="5.2" width="8" height="5.6" rx=".6" fill="#1a1a1b"/><path d="M4.3 5.6 8 8.4l3.7-2.8" stroke="#fff" stroke-width=".8" fill="none"/></svg>
          owen.thackery@coralbaysmile.example
        </li>
        <li>
          <svg viewBox="0 0 16 16" aria-hidden="true"><circle cx="8" cy="8" r="8" fill="#fff"/><circle cx="8" cy="8" r="4" fill="none" stroke="#1a1a1b" stroke-width="1"/><path d="M4 8h8M8 4c-1.6 2.4-1.6 5.6 0 8M8 4c1.6 2.4 1.6 5.6 0 8" stroke="#1a1a1b" stroke-width=".8" fill="none"/></svg>
          www.coralbaysmile.example
        </li>
      </ul>
    </div>
  </section>

</main>
</body>
</html>
```